Dorvel519 Smoke shop and Wine Store

DORVEL SMOKE SHOP & WINE INC

Smoke shop, Bill payments, unlock phones,Cellphones, Cellphone accessories and repair.
ADDRESS:
519 Harlow Ave11472Brooklyn, NY
phone # 3470182947
Mobile # 3470264813
E-mail: Dorvel5196@mailbrisk.com
Instagram: DORVELSMOKESHOP

we sell hookah and all hookah accessories and tobaccos. E-cigarettes, vapes, E-juice, vapes parts and replacements, unlocked phones, bill payments and international to-ups,

Target Market(s)

SMOKE sHOPS
Cell phones market

Industry/Entity Type

Shop

Contact Information for Business Card

Tarek Homsi
3470182947
3470264813

Smoke Shop - Unlocked phones - Phone Accessories - phone repair - bill payments - unlock services.

Font styles to use
Decorative

Requirements
Must have
• - attractive colors and designs on the business card.
• - graphics
Nice to have
• Cellphone pics and graphs

```html
<!DOCTYPE html>
<html lang="en">
<head>
<meta charset="utf-8">
<title>Dorvel Smoke Shop &amp; Wine Inc — Business Card</title>
<link rel="stylesheet" href="https://fonts.googleapis.com/css2?family=Jost:wght@400;500;600&family=Cookie&display=swap">
<style>
  :root {
    --card-black: #050306;
    --band-purple: #5a2a6e;
    --band-edge: #f2eef4;
    --text-white: #ffffff;
    --script-outline: #2a1a2a;
  }
  html, body { margin: 0; padding: 0; overflow: hidden; background: var(--card-black); }
  .card {
    position: relative;
    width: 1200px;
    height: 704px;
    overflow: hidden;
    background: var(--card-black);
    font-family: "Jost", "Futura", sans-serif;
    color: var(--text-white);
  }
  .card-art { position: absolute; inset: 0; }
  .brand-name {
    position: absolute;
    left: 105px; top: 145px;
    width: 290px;
    text-align: center;
    font-weight: 600;
    font-size: 62px;
    letter-spacing: 1px;
    color: var(--text-white);
  }
  .title-script {
    position: absolute;
    font-family: "Cookie", cursive;
    color: var(--text-white);
    -webkit-text-stroke: 2px var(--script-outline);
    text-shadow: 0 4px 8px rgba(0,0,0,.7);
    line-height: 1;
    white-space: nowrap;
  }
  .title-line-1 { left: 505px; top: 100px; font-size: 168px; }
  .title-line-2 { left: 690px; top: 198px; font-size: 160px; }
  .title-line-2 .suffix { font-size: 90px; }
  .contact-name {
    position: absolute; left: 81px; top: 362px;
    font-weight: 600; font-size: 39px; letter-spacing: 1.5px;
  }
  .contact-list { position: absolute; left: 78px; top: 430px; margin: 0; padding: 0; list-style: none; }
  .contact-item {
    position: relative; padding-left: 66px; height: 51px;
    font-size: 31px; line-height: 44px; letter-spacing: .5px;
  }
  .contact-item svg { position: absolute; left: 0; top: 6px; }
  .address {
    position: absolute; left: 780px; top: 532px;
    font-size: 31px; line-height: 51px; letter-spacing: .5px;
  }
</style>
</head>
<body>
<div class="card">
  <svg class="card-art" width="1200" height="704" viewBox="0 0 1200 704">
    <defs>
      <linearGradient id="photoTone" x1="0" y1="0" x2="1" y2="0">
        <stop offset="0" stop-color="#3a1a20"/>
        <stop offset=".3" stop-color="#8a3a44"/>
        <stop offset=".55" stop-color="#5a1e26"/>
        <stop offset="1" stop-color="#6a5a60"/>
      </linearGradient>
      <radialGradient id="swirlTone" cx=".7" cy=".55" r=".45">
        <stop offset="0" stop-color="#4a2360" stop-opacity=".9"/>
        <stop offset="1" stop-color="#050306" stop-opacity="0"/>
      </radialGradient>
      <path id="lowerArc" d="M40 238 C170 290 360 292 478 218"/>
      <path id="upperArc" d="M640 128 C820 72 1010 74 1192 126"/>
    </defs>
    <rect class="swirl-area" x="450" y="150" width="750" height="500" fill="url(#swirlTone)" role="img" aria-label="Faint purple smoke swirl"/>
    <path class="photo-collage" role="img" aria-label="Collage of hookah, smartphones, wine glass, beer, cigars and vape pens"
      d="M0 0 H1200 V150 C1000 112 760 112 600 150 C500 175 470 215 440 225 C330 262 200 262 0 210 Z" fill="url(#photoTone)"/>
    <path class="band-shade" d="M0 210 C200 262 330 262 440 225 C470 215 500 175 600 150 L520 228 C380 318 150 318 0 262 Z" fill="#1a0b22"/>
    <path class="arc-band" d="M0 268 C150 320 380 312 520 228 C640 156 900 124 1200 160"
      fill="none" stroke="var(--band-edge)" stroke-width="28"/>
    <path class="arc-band" d="M0 268 C150 320 380 312 520 228 C640 156 900 124 1200 160"
      fill="none" stroke="var(--band-purple)" stroke-width="18"/>
    <text font-family="Jost, sans-serif" font-weight="600" font-size="19" fill="#ffffff">
      <textPath href="#lowerArc" startOffset="6">BEER • CIGARETTES • E-CIGS • CIGARS • HOOKAH</textPath>
    </text>
    <text font-family="Jost, sans-serif" font-weight="600" font-size="17" fill="#ffffff">
      <textPath href="#upperArc" startOffset="4">• CELLPHONES, REPAIRS &amp; ACCESSORIES • BILL PAYMENTS</textPath>
    </text>
  </svg>

  <div class="brand-name">Dorvel</div>

  <div class="title-script title-line-1">Smoke Shop</div>
  <div class="title-script title-line-2">&amp; Wine <span class="suffix">inc</span></div>

  <div class="contact-name">TAREK HOMSI</div>
  <ul class="contact-list">
    <li class="contact-item">
      <svg width="34" height="34" viewBox="0 0 24 24"><path fill="#fff" d="M6.6 10.8a15.1 15.1 0 0 0 6.6 6.6l2.2-2.2c.3-.3.7-.4 1-.2 1.1.4 2.3.6 3.6.6.6 0 1 .4 1 1V20c0 .6-.4 1-1 1C10.6 21 3 13.4 3 4c0-.6.4-1 1-1h3.5c.6 0 1 .4 1 1 0 1.3.2 2.5.6 3.6.1.3 0 .7-.2 1z"/></svg>
      (347) 018 2947
    </li>
    <li class="contact-item">(347) 026 4813</li>
    <li class="contact-item">
      <svg width="38" height="34" viewBox="0 0 38 34"><path fill="#fff" d="M2 12 L19 2 L36 12 V32 H2 Z"/><text x="19" y="27" text-anchor="middle" font-family="Jost, sans-serif" font-size="14" font-weight="600" fill="#050306">@</text></svg>
      Dorvel5196@mailbrisk.com
    </li>
    <li class="contact-item">
      <svg width="34" height="34" viewBox="0 0 34 34"><rect x="2" y="2" width="30" height="30" rx="6" fill="#fff"/></svg>
      dorvelsmokeshop
    </li>
  </ul>

  <div class="address">519 Harlow Ave,<br>Brooklyn, NY 11472</div>
</div>
</body>
</html>
```